Kelvane Plumbing Business cards

Company is Kelvane Plumbing.
name Dashel Morrowby, I am a plumber, drainer, gasfitter and roofer
Mobile: 0431 906 154
Email address: info@kelvaneplumbing.example (check out my website for some ideas)
Website: www.kelvaneplumbing.example
ABN: 82 916 203 471
LIC: 604517K

I am reliable all round plumber. I am a 24 hour emergency service. Kelvane Plumbing is a professional plumbing service in the Illawarra, South Coast, Southern Sydney and Southern Highland regions of NSW. We offer a 24 hour emergency service for piece of mind to our customers. Call us now to see how we can help you. Kelvane Plumbing approaches every job with attention to detail and excellent customer service. With our superior workmanship you can be confident that the job will be done right the first time around. You can rest assured with results that are guaranteed to last.

Target Market(s)

the general public

Contact Information for Business Card

look up website for some ideas something with similar colours to logo and new modern and to catch the eye.

Colors
fdfdfd
ffffff
000000
7f7f7f
aaaaaa
33a6d7
0492cd

Requirements
Must have
• all contact details
• company- Kelvane Plumbing
• name- Dashel Morrowby
• number mobile- 0431 906 154
• Email address- info@kelvaneplumbing.example
• Website- www.kelvaneplumbing.example
• ABN- 82 916 203 471
• LIC- 604517K

```html
<!DOCTYPE html>
<html lang="en">
<head>
<meta charset="utf-8">
<title>Kelvane Plumbing – Business Cards</title>
<link href="https://fonts.googleapis.com/css2?family=Arimo:wght@400;700&display=swap" rel="stylesheet">
<style>
  :root {
    --stage: #2b2b2d;
    --card: #1f1f21;
    --card-edge: #2a2a2c;
    --blue: #0492cd;
    --blue-light: #33a6d7;
    --grey: #7f7f7f;
    --grey-light: #aaaaaa;
    --white: #fdfdfd;
    --rule: #d9d9d9;
  }
  * { margin: 0; padding: 0; box-sizing: border-box; }
  html, body { width: 1200px; height: 924px; overflow: hidden; }
  body {
    background: var(--stage);
    font-family: "Arimo", Arial, sans-serif;
    position: relative;
  }
  .card {
    position: absolute;
    width: 620px;
    height: 379px;
    background: var(--card);
    border: 1px solid var(--card-edge);
    border-radius: 3px;
    box-shadow: 0 18px 40px rgba(0,0,0,0.45);
    overflow: hidden;
  }
  .card--front { left: 290px; top: 60px; }
  .card--back  { left: 290px; top: 485px; }

  /* Front */
  .front-brand {
    position: absolute;
    inset: 0;
    display: flex;
    align-items: center;
    justify-content: center;
    gap: 16px;
  }
  .brand-dot {
    width: 22px; height: 22px;
    border-radius: 50%;
    background: var(--blue);
  }
  .brand-name {
    color: var(--blue);
    font-weight: 700;
    font-size: 34px;
    letter-spacing: 1px;
    text-transform: uppercase;
  }

  /* Back */
  .back-decor {
    position: absolute;
    left: 70px; top: 14px;
    width: 150px; height: 150px;
    border-radius: 50%;
    background: radial-gradient(circle, rgba(255,255,255,0.06), rgba(255,255,255,0) 70%);
  }
  .back-brand {
    position: absolute;
    right: 40px; top: 96px;
    color: var(--blue);
    font-weight: 700;
    font-size: 30px;
    letter-spacing: 1px;
    text-transform: uppercase;
  }
  .holder {
    position: absolute;
    left: 40px; top: 130px;
    width: 330px;
  }
  .holder-name {
    color: var(--blue-light);
    font-size: 19px;
    font-weight: 700;
    text-transform: uppercase;
    letter-spacing: 0.5px;
  }
  .holder-role {
    color: var(--grey);
    font-size: 13px;
    text-transform: uppercase;
    margin-top: 4px;
  }
  .holder-rule {
    height: 1px;
    background: var(--rule);
    margin-top: 8px;
    width: 560px;
  }
  .contact-list {
    list-style: none;
    margin-top: 12px;
  }
  .contact-list li {
    display: flex;
    align-items: center;
    gap: 12px;
    color: var(--white);
    font-size: 14px;
    line-height: 22px;
  }
  .contact-list svg { width: 14px; height: 14px; flex: none; }
  .registration {
    position: absolute;
    right: 40px; bottom: 36px;
    text-align: right;
    color: var(--white);
    font-size: 14px;
    line-height: 22px;
  }
  .registration-rule {
    position: absolute;
    right: 40px; bottom: 96px;
    width: 220px; height: 1px;
    background: var(--rule);
  }
</style>
</head>
<body>

  <section class="card card--front">
    <div class="front-brand">
      <span class="brand-dot"></span>
      <span class="brand-name">Kelvane Plumbing</span>
    </div>
  </section>

  <section class="card card--back">
    <div class="back-decor" role="img" aria-label="Faint brand emblem area"></div>
    <div class="back-brand">Kelvane Plumbing</div>

    <div class="holder">
      <div class="holder-name">Dashel Morrowby</div>
      <div class="holder-role">Plumber, Drainer, Gasfitter and Roofer</div>
      <div class="holder-rule"></div>
      <ul class="contact-list">
        <li>
          <svg viewBox="0 0 14 14" aria-hidden="true"><rect x="3.5" y="0.5" width="7" height="13" rx="1.5" fill="none" stroke="#0492cd" stroke-width="1.2"/><circle cx="7" cy="11.3" r="0.8" fill="#0492cd"/></svg>
          0431 906 154
        </li>
        <li>
          <svg viewBox="0 0 14 14" aria-hidden="true"><rect x="0.5" y="2.5" width="13" height="9" fill="#0492cd"/><path d="M0.5 2.5 L7 8 L13.5 2.5" fill="none" stroke="#1f1f21" stroke-width="1.2"/></svg>
          info@kelvaneplumbing.example
        </li>
        <li>
          <svg viewBox="0 0 14 14" aria-hidden="true"><circle cx="7" cy="7" r="6" fill="none" stroke="#0492cd" stroke-width="1.2"/><ellipse cx="7" cy="7" rx="2.6" ry="6" fill="none" stroke="#0492cd" stroke-width="1"/><line x1="1" y1="7" x2="13" y2="7" stroke="#0492cd" stroke-width="1"/></svg>
          www.kelvaneplumbing.example
        </li>
      </ul>
    </div>

    <div class="registration-rule"></div>
    <div class="registration">
      ABN - 82 916 203 471<br>
      LIC- 604517K
    </div>
  </section>

</body>
</html>
```